Newsletter template

I am looking for 2 newsletter templates. My website is in Wordpress and I want to use in mailchimp for lists.

One newsletter is for local clients of design remodeling firm to be sent monthly

Second newsletter is for web store offerings to be sent weekly.

Target Market(s)

Luxury home and leisure

Industry/Entity Type

Store

Requirements
Must have
• Use logos and colors to seamlessly integrate with website,

```html
<!DOCTYPE html>
<html lang="en">
<head>
<meta charset="utf-8">
<title>Wren Halloway — Newsletter</title>
<link href="https://fonts.googleapis.com/css2?family=Arimo:wght@400;700&family=Open+Sans:wght@400&display=swap" rel="stylesheet">
<style>
  :root {
    --accent: #1a9fc4;
    --accent-bright: #2bb7cf;
    --rule-blue: #5aa8cc;
    --tag-yellow: #dde000;
    --text-body: #777777;
    --media-dark: #444444;
    --button-light: #a9a9a9;
    --button-dark: #767676;
    --tab-dark: #3a3a3a;
    --page: #ffffff;
  }
  * { margin: 0; padding: 0; box-sizing: border-box; }
  html, body { width: 1200px; height: 2211px; overflow: hidden; background: var(--page); }
  body { position: relative; font-family: "Arimo", Arial, sans-serif; color: var(--text-body); }
  .abs { position: absolute; }

  .tab {
    left: 92px; top: 0; width: 316px; height: 92px;
    background: linear-gradient(#4a4a4a, var(--tab-dark));
    box-shadow: 0 4px 8px rgba(0,0,0,.25);
    border-top: 1px dashed #666;
    color: #fff; font-family: "Open Sans", sans-serif; font-size: 29px;
    text-align: center; line-height: 88px;
  }
  .utility-links {
    right: 92px; top: 4px; font-size: 17px; color: var(--accent);
  }
  .utility-links span { color: #555; padding: 0 4px; }
  .brand {
    left: 0; width: 1200px; top: 110px; text-align: center;
    font-size: 62px; font-weight: 400; color: var(--accent); letter-spacing: 1px;
  }
  .divider {
    left: 92px; width: 1016px; height: 10px;
    background: radial-gradient(ellipse at center, #d2d2d2 0%, #ececec 45%, rgba(255,255,255,0) 75%);
  }
  .thin-rule { left: 92px; width: 1016px; height: 1px; background: linear-gradient(to right, rgba(0,0,0,0), #ddd, rgba(0,0,0,0)); }
  .media { background: var(--media-dark); }
  .blue-rule { left: 92px; top: 753px; width: 1016px; height: 7px; background: var(--rule-blue); }
  .headline { color: var(--accent); font-size: 29px; font-weight: 400; line-height: 1.1; }
  .body-copy { font-size: 19px; line-height: 32.5px; color: var(--text-body); }
  .tag {
    background: var(--tag-yellow); color: #fff; font-weight: 700; font-size: 16.5px;
    height: 37px; line-height: 37px; padding: 0 13px; text-transform: uppercase;
  }
  .button {
    color: #fff; font-weight: 700; font-size: 17px; text-align: center;
    letter-spacing: 1px; text-transform: uppercase;
    box-shadow: 0 3px 3px rgba(0,0,0,.2);
  }
  .button--accent { background: var(--accent-bright); }
  .button--light { background: var(--button-light); }
  .button--dark { background: var(--button-dark); }
</style>
</head>
<body>
  <div class="abs tab">newsletter</div>
  <div class="abs utility-links">browser version<span>•</span>text version<span>•</span>unsubscribe</div>
  <div class="abs brand">Wren Halloway</div>

  <div class="abs divider" style="top:253px"></div>

  <div class="abs media" style="left:92px;top:302px;width:1016px;height:419px" role="img" aria-label="Featured lifestyle photograph"></div>

  <div class="abs blue-rule"></div>
  <h1 class="abs headline" style="left:92px;top:793px">Non semper lorem sollicitudin</h1>
  <div class="abs button button--accent" style="left:948px;top:794px;width:160px;height:37px;line-height:37px">View More</div>
  <p class="abs body-copy" style="left:92px;top:851px;width:830px">Donec porttitor quam vel purus venenatis rutrum. Nullam quam nibh, congue sed aliquet posuere, aliquam non lacus. Maecenas nec luctus neque. Aliquam sagittis tincidunt lectus, non semper lorem sollicitudin ac. Proin ac felis tortor, eu ultricies orci.</p>

  <div class="abs divider" style="top:992px"></div>

  <article>
    <div class="abs tag" style="left:92px;top:1047px">The Special One Article</div>
    <h2 class="abs headline" style="left:92px;top:1109px">Quisque convallis</h2>
    <p class="abs body-copy" style="left:92px;top:1158px;width:500px">Donec porttitor quam vel purus venenatis rutrum. Nullam quam nibh, congue sed aliquet posuere, aliquam non lacus. Maecenas nec luctus neque...</p>
    <div class="abs button button--light" style="left:92px;top:1290px;width:103px;height:36px;line-height:36px">More</div>
    <div class="abs media" style="left:616px;top:1047px;width:492px;height:277px" role="img" aria-label="Article photograph"></div>
  </article>

  <div class="abs thin-rule" style="top:1363px"></div>

  <article>
    <div class="abs tag" style="left:92px;top:1397px">Flexible</div>
    <h2 class="abs headline" style="left:92px;top:1459px">Sed eu laoreet metus</h2>
    <p class="abs body-copy" style="left:92px;top:1508px;width:500px">Donec porttitor quam vel purus venenatis rutrum. Nullam quam nibh, congue sed aliquet posuere, aliquam non lacus. Maecenas nec luctus neque...</p>
    <div class="abs button button--dark" style="left:92px;top:1640px;width:103px;height:36px;line-height:36px">View</div>
    <div class="abs media" style="left:616px;top:1397px;width:492px;height:277px" role="img" aria-label="Article photograph"></div>
  </article>

  <div class="abs divider" style="top:1721px"></div>

  <div class="abs media" style="left:92px;top:1777px;width:1016px;height:129px" role="img" aria-label="Promotional banner image"></div>

  <div class="abs divider" style="top:1950px"></div>

  <article>
    <div class="abs" style="left:145px;top:2032px;width:226px;height:179px;background:linear-gradient(135deg,#f4f4f4,#dcdcdc)" role="img" aria-label="Product photograph of a book"></div>
    <div class="abs tag" style="left:437px;top:2003px">Special Price: 8$</div>
    <h2 class="abs headline" style="left:437px;top:2062px;font-size:34px">Vivamus Vivamus</h2>
    <p class="abs body-copy" style="left:437px;top:2112px;width:680px">Donec porttitor quam vel purus venenatis rutrum. Nullam quam nibh, congue sed aliquet posuere, aliquam non lacus. Maecenas nec luctus neque...</p>
    <div class="abs button button--dark" style="left:437px;top:2205px;width:105px;height:36px"></div>
    <div class="abs button button--accent" style="left:550px;top:2205px;width:105px;height:36px"></div>
  </article>
</body>
</html>
```